Bright Summit Web Design

I am starting a new company that will provide LIFE COACHING services - I have tried to design a website, but it's too complicated. Right now, it's just me - I'm the only person that will provide services through the website - I have used makerhive to purchase a logo (see below). I want to be able to update the website myself, but need a template - basic design. Because I am not technologically savvy enough to explain in words - I basically want to have a website that will provide basic information about my services (coaching), a page about me and my background, hopefully scheduling possibilities, and testimonials — also a page for writing/blogs. I bought a website through NetBarn - so when I have a template, I guess I”d use that - but maybe I’ll need to work with a designer to actually get it up on the internet. I have a head shot that I’ll upload, too.
Clients from the independent (private school) world - teachers, administrators
4 page

```html
<!DOCTYPE html>
<html lang="en">
<head>
<meta charset="utf-8">
<title>Bright Summit Coaching</title>
<link href="https://fonts.googleapis.com/css2?family=Marcellus&family=Barlow:wght@400;500;600;700;800&family=Montserrat:wght@500;600;700&display=swap" rel="stylesheet">
<style>
:root{
  --teal:#19a998;
  --teal-dark:#0e9483;
  --teal-soft:#5cc6b8;
  --mint:#eaf6f4;
  --mint-2:#f2f9f8;
  --ink:#2b2b2b;
  --body:#4a4a4a;
  --muted:#8a8a8a;
  --white:#ffffff;
  --line:#cfe7e3;
}
*{box-sizing:border-box;margin:0;padding:0}
html,body{width:1200px;height:5000px;overflow:hidden;background:var(--white)}
body{position:relative;font-family:"Barlow",sans-serif;color:var(--body)}
section,header,footer{position:absolute;left:0;width:1200px}
.abs{position:absolute}
.serif{font-family:"Marcellus",serif;font-weight:400}
.eyebrow{font-family:"Barlow",sans-serif;color:var(--teal);font-size:17px;letter-spacing:.5px;text-transform:uppercase}
.section-title{font-family:"Marcellus",serif;font-size:36px;color:var(--ink);letter-spacing:2px;text-transform:uppercase}
.rule{height:2px;width:90px;background:var(--teal)}
.center{left:0;width:1200px;text-align:center}
.btn-outline{position:absolute;border:2px solid var(--teal);border-radius:30px;color:var(--teal);font-family:"Barlow",sans-serif;font-weight:700;letter-spacing:1.5px;font-size:14px;text-transform:uppercase;display:flex;align-items:center;justify-content:center;background:rgba(255,255,255,.6)}
.photo{position:absolute;border-radius:50%}

/* header */
.site-header{top:0;height:78px;background:rgba(255,255,255,.92);z-index:5}
.brand-badge{position:absolute;left:92px;top:4px;width:196px;height:150px;border-radius:50%;background:var(--white);display:flex;align-items:center;justify-content:center;z-index:6}
.brand-name{font-family:"Marcellus",serif;font-size:21px;color:#555;letter-spacing:1px}
.nav a{position:absolute;top:30px;font-family:"Barlow",sans-serif;font-size:14px;font-weight:500;color:#222;text-decoration:none;text-transform:uppercase;letter-spacing:.3px}
.nav a.active{color:var(--teal)}
.nav .active-bar{position:absolute;left:330px;top:74px;width:80px;height:3px;background:var(--teal)}
.cta{position:absolute;left:909px;top:19px;width:214px;height:44px;border-radius:24px;background:var(--teal);color:var(--white);font-weight:700;font-size:13px;letter-spacing:.4px;display:flex;align-items:center;justify-content:center;gap:8px;text-transform:uppercase}

/* hero */
.hero{top:0;height:790px}
.hero-photo{position:absolute;left:0;top:0;width:1200px;height:777px;background:linear-gradient(100deg,#c99978 0%,#e9dccf 30%,#efe7de 55%,#cdb7a2 80%,#8d7a6c 100%)}
.hero-text{position:absolute;top:292px}
.hero-welcome{font-family:"Marcellus",serif;font-size:24px;color:#4a4a4a;letter-spacing:2px}
.hero-title{font-family:"Marcellus",serif;font-size:54px;line-height:54px;color:#333;letter-spacing:2px}
.hero-title .accent{color:var(--teal)}
.down-arrow{position:absolute;left:571px;top:625px;width:54px;height:54px;border-radius:50%;background:var(--teal)}

/* about */
.about{top:800px;height:590px}
.about-copy{position:absolute;left:591px;width:480px;text-align:center}
.about-copy p{font-size:19px;line-height:27px;color:#444}

/* services */
.services{top:1398px;height:1349px;background:var(--mint)}
.service-heading{font-family:"Montserrat",sans-serif;font-weight:600;font-size:22px;line-height:31px;color:#222;letter-spacing:.8px;text-transform:uppercase}
.service-text{font-size:15.5px;line-height:27px;color:#444;margin-top:14px}
.service-ring{position:absolute;width:312px;height:312px;border-radius:50%;border:2px solid var(--teal-soft)}
.service-ring .photo{left:14px;top:14px;width:280px;height:280px;background:radial-gradient(circle at 40% 40%,#5fcdbb,#149e8c)}

/* blogs */
.blogs{top:2747px;height:600px}
.card{position:absolute;top:111px;width:319px;height:410px;border:2px solid var(--line);border-radius:28px 0 28px 0;background:var(--white);overflow:hidden}
.card-img{position:absolute;left:0;top:0;width:100%;height:214px}
.card-date{position:absolute;left:8px;top:197px;height:26px;padding:0 10px;background:var(--teal);color:var(--white);font-size:12px;font-family:"Montserrat",sans-serif;font-weight:600;display:flex;align-items:center;gap:6px}
.card-title{position:absolute;left:28px;top:240px;width:270px;font-family:"Montserrat",sans-serif;font-weight:600;font-size:17px;line-height:22px;color:#222}
.card-text{position:absolute;left:28px;top:292px;width:270px;font-size:13.5px;line-height:20px;color:#444}
.card .btn-outline{left:28px;top:344px;width:132px;height:38px;font-size:11px}

/* testimonials */
.testimonials{top:3355px;height:630px}
.testimonials-bg{position:absolute;left:0;top:0;width:1200px;height:630px;background:linear-gradient(180deg,rgba(255,255,255,0) 75%,rgba(242,249,248,.35) 100%),linear-gradient(115deg,#52c4b4 0%,#1fae9c 55%,#17a593 100%)}
.avatar{position:absolute;border-radius:50%;border:3px solid var(--white)}
.quote-mark{position:absolute;color:var(--white);font-family:"Barlow",sans-serif;font-weight:800;font-size:84px;line-height:84px}
.quote{position:absolute;left:300px;top:292px;width:600px;text-align:center;color:var(--white);font-size:19px;line-height:31px}
.quote-name{position:absolute;top:402px;color:var(--white);font-weight:700;font-size:20px}

/* appointment */
.appointment{top:3985px;height:660px;background:var(--mint-2)}
.field{position:absolute;height:40px;border:1px solid #bfc9c7;background:var(--white);font-size:13px;color:#777;padding:0 14px;display:flex;align-items:center;gap:6px}
.book-btn{position:absolute;left:138px;top:426px;width:182px;height:49px;border-radius:26px;background:var(--teal);color:var(--white);font-weight:700;font-size:15px;letter-spacing:1.5px;display:flex;align-items:center;justify-content:center}

/* footer */
.site-footer{top:4630px;height:370px}
.foot-col{position:absolute;top:60px;height:240px;border-left:2px solid var(--teal)}
.foot-head{font-family:"Montserrat",sans-serif;font-weight:600;font-size:14px;color:#333;letter-spacing:.6px}
.foot-list{list-style:none;margin-top:12px}
.foot-list li{font-size:14px;color:#555;line-height:25.5px}
.foot-text{font-size:13.5px;color:#555;line-height:20px}
.social{position:absolute;top:4747px;width:32px;height:32px;border-radius:50%;background:var(--teal)}
.copyright{position:absolute;left:0;top:4941px;width:1200px;height:59px;background:#e4f1ef;display:flex;align-items:center;justify-content:center;font-size:12.5px;color:#666}
</style>
</head>
<body>

<!-- Header -->
<header class="site-header">
  <div class="brand-badge"><span class="brand-name">BRIGHT SUMMIT</span></div>
  <nav class="nav">
    <a class="active" style="left:334px">About Us</a>
    <a style="left:450px">Services</a>
    <a style="left:564px">Blogs</a>
    <a style="left:657px">Testimonials</a>
    <a style="left:805px">Contact</a>
    <span class="active-bar"></span>
  </nav>
  <div class="cta">
    <svg width="14" height="14" viewBox="0 0 14 14"><rect x="1" y="2.5" width="12" height="10.5" rx="1" fill="none" stroke="#fff" stroke-width="1.5"/><line x1="1" y1="6" x2="13" y2="6" stroke="#fff" stroke-width="1.5"/><line x1="4" y1="0.5" x2="4" y2="4" stroke="#fff" stroke-width="1.5"/><line x1="10" y1="0.5" x2="10" y2="4" stroke="#fff" stroke-width="1.5"/></svg>
    Schedule Appointment
  </div>
</header>

<!-- Hero -->
<section class="hero">
  <div class="hero-photo" role="img" aria-label="Photo of a coach in conversation with a smiling client in a bright room"></div>
  <div class="hero-text center">
    <div class="hero-welcome">WELCOME TO</div>
    <div class="hero-title" style="margin-top:10px">BRIGHT SUMMIT<br><span class="accent">COACHING</span></div>
  </div>
  <div class="btn-outline" style="left:512px;top:452px;width:175px;height:49px">Learn More</div>
  <div class="down-arrow">
    <svg width="54" height="54" viewBox="0 0 54 54"><path d="M27 16 V37 M19 29 L27 37 L35 29" fill="none" stroke="#fff" stroke-width="2.5" stroke-linecap="round" stroke-linejoin="round"/></svg>
  </div>
</section>

<!-- About -->
<section class="about">
  <svg class="abs" style="left:70px;top:60px" width="520" height="520" viewBox="0 0 520 520">
    <circle cx="250" cy="237" r="240" fill="none" stroke="#19a998" stroke-width="2.5"/>
    <circle cx="250" cy="237" r="228" fill="none" stroke="#19a998" stroke-width="1"/>
  </svg>
  <div class="photo" role="img" aria-label="Head shot of the coach" style="left:112px;top:89px;width:416px;height:416px;background:radial-gradient(circle at 50% 45%,#e9d9c4 0%,#d4e8e4 55%,#b9ddd6 100%)"></div>
  <div class="about-copy" style="top:104px">
    <div class="eyebrow" style="font-size:20px">About Me</div>
    <div class="serif" style="font-size:44px;color:#333;letter-spacing:2px;margin-top:4px">CLAIRE HOLLANDER</div>
    <p style="margin-top:24px">Claire has over 35 years experience teaching and leading in independent schools, including eleven as Head of School. Her coaching practice focuses on independent schools, supporting teachers, administrators, Board members, and parents as they navigate their own Bright Summit.</p>
  </div>
  <div class="btn-outline" style="left:753px;top:394px;width:179px;height:49px">Learn More</div>
</section>

<!-- Services -->
<section class="services">
  <div class="abs center" style="top:42px"><div class="eyebrow">What We Offer</div></div>
  <div class="abs center section-title" style="top:66px">Coaching Service</div>
  <div class="rule abs" style="left:555px;top:117px"></div>

  <svg class="abs" style="left:0;top:0" width="1200" height="1349" viewBox="0 0 1200 1349">
    <path d="M662 400 V440 Q662 458 644 458 H494 Q476 458 476 476 V516" fill="none" stroke="#5cc6b8" stroke-width="2"/>
    <path d="M476 762 V796 Q476 814 494 814 H644 Q662 814 662 832 V876" fill="none" stroke="#5cc6b8" stroke-width="2"/>
    <path d="M0 1349 L0 1290 Q600 1210 1200 1290 L1200 1349 Z" fill="#fff"/>
    <path d="M180 1315 Q600 1225 1060 1310" fill="none" stroke="#19a998" stroke-width="4"/>
  </svg>

  <div class="service-ring" style="left:194px;top:160px">
    <div class="photo" role="img" aria-label="Teal illustration of a mountain summit with flags"></div>
  </div>
  <div class="abs" style="left:627px;top:220px;width:420px">
    <div class="service-heading">Growing Your Goals</div>
    <div class="service-text">I help you re-imagine your life. With extensive experience as a certified professional coach and over thirty years of teaching and leadership experience, my individualized approach will help you attain your goals.</div>
  </div>

  <div class="abs" style="left:169px;top:546px;width:440px">
    <div class="service-heading">Guiding With<br>Professionalism</div>
    <div class="service-text">I help you re-imagine your life. With extensive experience as a certified professional coach and over thirty years of teaching and leadership experience, my individualized approach will help you attain your goals.</div>
  </div>
  <div class="service-ring" style="left:675px;top:485px">
    <div class="photo" role="img" aria-label="Teal illustration of two profiles sharing an idea"></div>
  </div>

  <div class="service-ring" style="left:197px;top:850px">
    <div class="photo" role="img" aria-label="Teal illustration of a path between two people"></div>
  </div>
  <div class="abs" style="left:602px;top:940px;width:450px">
    <div class="service-heading">Giving You Voice</div>
    <div class="service-text">Committing to new choices and opportunities is just that – a commitment, and it's a big one that will take a lot a dedication. My commitment is to hear you and support with accountability, understanding and encouragement.</div>
  </div>

  <div class="btn-outline" style="left:509px;top:1162px;width:169px;height:48px">Learn More</div>
</section>

<!-- Blogs -->
<section class="blogs">
  <div class="abs center" style="top:0"><div class="eyebrow">Recent Posts</div></div>
  <div class="abs center section-title" style="top:24px">Latest Blogs</div>
  <div class="rule abs" style="left:555px;top:74px"></div>

  <article class="card" style="left:113px">
    <div class="card-img" role="img" aria-label="Photo of a smiling woman at her desk holding a note" style="background:linear-gradient(120deg,#d9cbb8,#eae3d8 50%,#a9b89b)"></div>
    <div class="card-date"><svg width="11" height="11" viewBox="0 0 11 11"><rect x=".5" y="1.5" width="10" height="9" fill="none" stroke="#fff"/><line x1=".5" y1="4.5" x2="10.5" y2="4.5" stroke="#fff"/></svg>June 21, 2022</div>
    <div class="card-title">Sed ut perspiciatis unde omnis iste natus error</div>
    <div class="card-text">Lorem ipsum dolor sit amet cons ecte tur adipiscing dolor sit amet cons</div>
    <div class="btn-outline">Learn More</div>
  </article>
  <article class="card" style="left:452px">
    <div class="card-img" role="img" aria-label="Photo of two women talking at a table" style="background:linear-gradient(120deg,#efeae4,#d6c7b6 50%,#6c5a4d)"></div>
    <div class="card-date"><svg width="11" height="11" viewBox="0 0 11 11"><rect x=".5" y="1.5" width="10" height="9" fill="none" stroke="#fff"/><line x1=".5" y1="4.5" x2="10.5" y2="4.5" stroke="#fff"/></svg>June 17, 2022</div>
    <div class="card-title">Sed ut perspiciatis unde omnis iste natus error</div>
    <div class="card-text">Lorem ipsum dolor sit amet cons ecte tur adipiscing dolor sit amet cons</div>
    <div class="btn-outline">Learn More</div>
  </article>
  <article class="card" style="left:794px">
    <div class="card-img" role="img" aria-label="Photo of two women in a coaching session near a staircase" style="background:linear-gradient(120deg,#bfc6c2,#e8e6e1 50%,#9fb3c6)"></div>
    <div class="card-date"><svg width="11" height="11" viewBox="0 0 11 11"><rect x=".5" y="1.5" width="10" height="9" fill="none" stroke="#fff"/><line x1=".5" y1="4.5" x2="10.5" y2="4.5" stroke="#fff"/></svg>June 10, 2022</div>
    <div class="card-title">Sed ut perspiciatis unde omnis iste natus error</div>
    <div class="card-text">Lorem ipsum dolor sit amet cons ecte tur adipiscing dolor sit amet cons</div>
    <div class="btn-outline">Learn More</div>
  </article>
</section>

<!-- Testimonials -->
<section class="testimonials">
  <div class="testimonials-bg"></div>
  <div class="abs center" style="top:65px;color:#fff;font-size:16px;letter-spacing:.5px">WHAT PEOPLE SAY</div>
  <div class="abs center serif" style="top:88px;color:#fff;font-size:38px;letter-spacing:2px">TESTIMONIALS</div>
  <div class="rule abs" style="left:555px;top:140px;background:#fff;opacity:.6"></div>

  <div class="avatar" role="img" aria-label="Client portrait" style="left:481px;top:197px;width:48px;height:48px;background:#b8b0a8"></div>
  <div class="avatar" role="img" aria-label="Client portrait" style="left:553px;top:176px;width:90px;height:90px;background:#d8c3b0;box-shadow:0 0 0 3px #19a998,0 0 0 5px #fff"></div>
  <div class="avatar" role="img" aria-label="Client portrait" style="left:669px;top:197px;width:48px;height:48px;background:#6f6058"></div>

  <svg class="abs" style="left:96px;top:278px" width="26" height="46" viewBox="0 0 26 46"><path d="M22 3 L4 23 L22 43" fill="none" stroke="#fff" stroke-width="3"/></svg>
  <svg class="abs" style="left:1082px;top:278px" width="26" height="46" viewBox="0 0 26 46"><path d="M4 3 L22 23 L4 43" fill="none" stroke="#fff" stroke-width="3"/></svg>

  <div class="quote-mark" style="left:258px;top:278px">&ldquo;</div>
  <div class="quote-mark" style="left:846px;top:358px">&rdquo;</div>
  <div class="quote">Lorem ipsum dolor sit amet consectetur adipiscing elit, sed do eiusmod tempor incididunt ut labore et dolore magna aliqua. Ut enim ad minim veniam, quis nostrud exercitation ullamco laboris nisi</div>
  <div class="quote-name center">Daniel Brooks</div>
</section>

<!-- Appointment -->
<section class="appointment">
  <div class="abs eyebrow" style="left:138px;top:120px;font-size:15px">Book Apointment Now</div>
  <div class="abs section-title" style="left:138px;top:144px;font-size:32px;letter-spacing:1.5px">Schedule an Appointment</div>

  <div class="field" style="left:138px;top:224px;width:225px">Name</div>
  <div class="field" style="left:371px;top:224px;width:225px">Email address</div>
  <div class="field" style="left:138px;top:275px;width:225px">Phone</div>
  <div class="field" style="left:371px;top:275px;width:225px">
    <svg width="11" height="11" viewBox="0 0 11 11"><rect x=".5" y="1.5" width="10" height="9" fill="none" stroke="#19a998"/><line x1=".5" y1="4.5" x2="10.5" y2="4.5" stroke="#19a998"/></svg>Select Date
  </div>
  <div class="field" style="left:138px;top:328px;width:458px;height:80px;align-items:flex-start;padding-top:12px">Message</div>
  <div class="book-btn">BOOK NOW</div>

  <svg class="abs" style="left:660px;top:150px" width="430" height="430" viewBox="0 0 430 430">
    <circle cx="214" cy="188" r="206" fill="none" stroke="#19a998" stroke-width="2.5"/>
  </svg>
  <div class="photo" role="img" aria-label="Photo of a woman in a hat enjoying the sunset outdoors" style="left:686px;top:150px;width:378px;height:378px;background:radial-gradient(circle at 35% 35%,#f3d6a0 0%,#d99a5a 45%,#7c4a35 100%)"></div>

  <svg class="abs" style="left:0;top:560px" width="1200" height="100" viewBox="0 0 1200 100">
    <path d="M0 100 L0 20 Q600 110 1200 20 L1200 100 Z" fill="#fff"/>
    <path d="M30 22 Q600 100 1170 22" fill="none" stroke="#19a998" stroke-width="4"/>
  </svg>
</section>

<!-- Footer -->
<footer class="site-footer">
  <div class="abs" style="left:123px;top:36px;width:200px;height:200px;border-radius:50%;border:2px solid var(--teal)"></div>
  <div class="abs brand-name" style="left:123px;top:123px;width:200px;text-align:center;font-size:22px">BRIGHT SUMMIT</div>

  <div class="foot-col" style="left:427px;padding-left:22px">
    <div class="foot-head" style="margin-top:10px">NAVIGATION</div>
    <ul class="foot-list">
      <li>&raquo; About Us</li>
      <li>&raquo; Services</li>
      <li>&raquo; Testimonials</li>
      <li>&raquo; Blogs</li>
      <li>&raquo; Contact Us</li>
    </ul>
  </div>
  <div class="foot-col" style="left:635px;padding-left:16px">
    <div class="foot-head" style="margin-top:10px">CONTACT US</div>
    <div style="position:relative;margin-top:16px;padding-left:34px">
      <svg class="abs" style="left:0;top:0" width="24" height="24" viewBox="0 0 24 24"><circle cx="12" cy="12" r="12" fill="#19a998"/><path d="M12 5.5c-2.5 0-4.3 1.9-4.3 4.3 0 3.2 4.3 8 4.3 8s4.3-4.8 4.3-8c0-2.4-1.8-4.3-4.3-4.3z" fill="#fff"/><circle cx="12" cy="9.8" r="1.6" fill="#19a998"/></svg>
      <div class="foot-text">2280 Maple Ridge Rd, Suite #140<br>Cedar Hollow, VA 24410</div>
    </div>
    <div style="position:relative;margin-top:16px;padding-left:34px">
      <svg class="abs" style="left:0;top:-3px" width="24" height="24" viewBox="0 0 24 24"><circle cx="12" cy="12" r="12" fill="#19a998"/><path d="M8.3 6.5l2 .2 1 2.6-1.4 1.1c.7 1.5 1.8 2.6 3.3 3.3l1.1-1.4 2.6 1 .2 2c-.6.8-1.6 1.2-2.6 1-4-.8-7-3.8-7.8-7.8-.2-1 .2-2 1-2.6z" fill="#fff"/></svg>
      <div class="foot-text">(555) 014-2290</div>
    </div>
  </div>
  <div class="foot-col" style="left:911px;padding-left:16px">
    <div class="foot-head" style="margin-top:10px">FOLLOW US</div>
  </div>
</footer>
<div class="social" role="img" aria-label="Social link" style="left:926px"></div>
<div class="social" role="img" aria-label="Social link" style="left:966px"></div>
<div class="social" role="img" aria-label="Social link" style="left:1006px"></div>
<div class="social" role="img" aria-label="Social link" style="left:1046px"></div>

<div class="copyright">&copy; 2022 Bright Summit Coaching All Rights Reserved</div>

</body>
</html>
```